"Brighter Harbors: Ways to guide growth via study" Co Authored by Dr Malcolm Penner & Lewis Brandt

We need a clean design book cover for "Brighter Harbors: Ways to guide growth via study." Co-authored by Dr Malcolm Penner and Lewis Brandt. (Malcolm Penner being the lead author)
This book tells the story of a new learning paradigm in business for successful transformation. Why and How you can make learning last.
We would like the design to work with - but not limited by - the current branding that we already have in place; please see www.drmalcolmpenner.example

Target Market(s)

Business decision makers.

Industry/Entity Type

Learning

Font styles to use
Sans Serif

Requirements
Must have
• A clean professional finish
Nice to have
• A picture, graphic or image of some sort tied to the brief
Should not have
• Be too busy in design.

```html
<!DOCTYPE html>
<html lang="en">
<head>
<meta charset="utf-8">
<title>Brighter Harbors – Book Cover</title>
<link href="https://fonts.googleapis.com/css2?family=Audiowide&family=Oswald:wght@500&family=Roboto+Condensed:wght@700&display=swap" rel="stylesheet">
<style>
  :root {
    --navy-deep: #0b1f52;
    --navy-mid: #0a3a86;
    --royal: #0a56a8;
    --cover-blue: #1462b4;
    --space-black: #05070d;
    --white: #ffffff;
    --ink: #111111;
  }
  * { margin: 0; padding: 0; box-sizing: border-box; }
  html, body { width: 1200px; height: 920px; overflow: hidden; }
  body { position: relative; background: var(--navy-deep); }
  .back-cover {
    position: absolute; left: 0; top: 0;
    width: 610px; height: 920px;
    background: linear-gradient(180deg, #0b1d4e 0%, var(--navy-mid) 28%, var(--royal) 50%, var(--navy-mid) 72%, #0b1d4e 100%);
  }
  .front-cover {
    position: absolute; left: 611px; top: 12px;
    width: 578px; height: 898px;
    background: var(--white);
    overflow: hidden;
  }
  .cover-art {
    position: absolute; left: 0; top: 0;
    width: 578px; height: 448px;
    background:
      radial-gradient(ellipse 60% 45% at 62% 30%, rgba(190,225,255,0.9) 0%, rgba(40,110,190,0.6) 18%, transparent 45%),
      radial-gradient(ellipse 62% 70% at 52% 78%, #1f5f9e 0%, #12355f 55%, transparent 75%),
      linear-gradient(180deg, var(--space-black) 0%, #0c1a30 60%, #1b3c66 100%);
  }
  .title-band {
    position: absolute; left: 0; top: 448px;
    width: 578px; height: 92px;
    background: var(--cover-blue);
  }
  .skyline-art {
    position: absolute; left: 0; top: 540px;
    width: 578px; height: 170px;
    background: linear-gradient(180deg, var(--cover-blue) 0%, #4d8bcb 45%, #c9ddf1 80%, var(--white) 100%);
  }
  .title {
    position: absolute; left: 0; width: 578px;
    text-align: center;
    font-family: 'Audiowide', sans-serif;
    font-weight: 400;
    font-size: 52px;
    line-height: 1;
    color: var(--white);
    letter-spacing: 2px;
    transform: scaleX(1.2);
    text-shadow: 0 2px 3px rgba(0,0,0,0.5);
  }
  .title-line1 { top: 388px; }
  .title-line2 { top: 452px; }
  .subtitle {
    position: absolute; left: 0; width: 578px; top: 524px;
    text-align: center;
    font-family: 'Oswald', sans-serif;
    font-weight: 500;
    font-size: 35px;
    line-height: 1;
    color: var(--white);
    text-shadow: 0 1px 2px rgba(0,0,0,0.6);
  }
  .author {
    position: absolute; left: 0; width: 578px;
    text-align: center;
    font-family: 'Roboto Condensed', sans-serif;
    font-weight: 700;
    font-size: 40px;
    color: var(--ink);
  }
  .author span {
    display: inline-block;
    border-bottom: 1.5px solid var(--ink);
    padding-bottom: 1px;
    line-height: 1.05;
  }
  .author-lead { top: 706px; }
  .author-co { top: 790px; }
</style>
</head>
<body>
  <div class="back-cover"></div>

  <section class="front-cover">
    <div class="cover-art" role="img" aria-label="Illustration of a city skyline in front of a glowing Earth against a starry night sky"></div>
    <div class="title-band"></div>
    <div class="skyline-art" role="img" aria-label="Blue city skyline silhouette dissolving into the white lower cover"></div>

    <h1 class="title title-line1">BRIGHTER</h1>
    <h1 class="title title-line2">HARBORS</h1>
    <p class="subtitle">WAYS TO GUIDE GROWTH VIA STUDY</p>

    <p class="author author-lead"><span>DR. MALCOLM PENNER</span></p>
    <p class="author author-co"><span>LEWIS BRANDT</span></p>
  </section>
</body>
</html>
```